Marketing Brochure design required by Video Production company

We are looking for a slick, professional and eye-catching design for a marketing brochure that will showcase our company and its services.

Purpose:
The purpose of the brochure is to show our company as experienced, capable, professional and creative.

The Brochure:
The brochure will be 10 pages (including front and back cover), designed for printing in measurements of 16cm (height) x 18cm (wide).

Attached you will find:

1. Brochure Copy/Text - this is all the text to be included in the brochure. Text in red colour is not to be included in the design but is there as a guide to assist in the design

2. Design assets - our logo and hi-resolution images to be included in the design. The filenames of the images correspond with pages in the Brochure Copy/Text (as you will see)
* this does not seem to be attaching here in ArtMarketHub. Please download this file from stashbin here: https://www.stashbin.net/s/qk4tr7wnz2lpa0e/Product_Marketing_Brochure_Assets-2016-02-07.zip?dl=0

Design:
We would like the design to be open - not cramped or squashed in. Use of space is good. We want it to look very professional, but creative. And also feel simple and easy to read.

Colours to use - blues with black & white (black & white is our brand).

Please feel free to ask any questions you might have.

Thank you.

Industry/Entity Type

It Company

Font styles to use
Sans Serif

Colors
0592cd
3176b5
3276b5
33a6d7
85cae6
cee9f5
85acd3
eaf1f7

Requirements
Must have
• As per the description.
• Download design assets from:
• https://www.stashbin.net/s/qk4tr7wnz2lpa0e/Product_Marketing_Brochure_Assets-2016-02-07.zip?dl=0

```html
<!DOCTYPE html>
<html lang="en">
<head>
<meta charset="utf-8">
<title>Video Production Brochure – Your Story / Your Event</title>
<link rel="stylesheet" href="https://fonts.googleapis.com/css2?family=Open+Sans:wght@300;400;700&display=swap">
<style>
  :root {
    --backdrop: #d9d4cb;
    --page: #ffffff;
    --ink: #2a2a2a;
    --ink-soft: #3c3c3c;
    --label-bg: #262626;
    --frame: #e4e4e4;
    --panel: rgba(24, 18, 40, 0.72);
    --white: #ffffff;
  }
  * { box-sizing: border-box; margin: 0; padding: 0; }
  html, body { width: 1200px; height: 600px; overflow: hidden; }
  body {
    background: var(--backdrop);
    font-family: "Open Sans", Arial, sans-serif;
    color: var(--ink);
    position: relative;
  }
  .spread {
    position: absolute; left: 20px; top: 42px;
    width: 1160px; height: 516px;
    display: flex;
    box-shadow: 0 4px 18px rgba(0,0,0,0.25);
  }
  .page { position: relative; width: 580px; height: 516px; overflow: hidden; }
  .page--story { background: var(--page); }

  /* Collage */
  .collage {
    position: absolute; left: 24px; top: 28px;
    width: 528px; height: 266px;
    background: var(--frame);
    padding: 5px;
    display: grid;
    grid-template-columns: 240px 158px 110px;
    grid-template-rows: repeat(12, 1fr);
    gap: 5px;
  }
  .shot { background: linear-gradient(135deg, #5a4a40, #2c2522); }
  .shot--a { grid-column: 1; grid-row: 1 / 7; background: linear-gradient(135deg, #4a3a30, #1f1a18); }
  .shot--b { grid-column: 1; grid-row: 7 / 13; background: linear-gradient(135deg, #b9c6d3, #6e7f8c); }
  .shot--c { grid-column: 2; grid-row: 1 / 5; background: linear-gradient(135deg, #6b5c55, #2f2a2a); }
  .shot--d { grid-column: 2; grid-row: 5 / 9; background: linear-gradient(135deg, #8a7a5a, #3b3a35); }
  .shot--e { grid-column: 2; grid-row: 9 / 13; background: linear-gradient(135deg, #3c3a3a, #1b1a1b); }
  .shot--f { grid-column: 3; grid-row: 1 / 4; background: linear-gradient(135deg, #9fb6c6, #d8d0c4); }
  .shot--g { grid-column: 3; grid-row: 4 / 7; background: linear-gradient(135deg, #6a3a32, #2a1b1a); }
  .shot--h { grid-column: 3; grid-row: 7 / 10; background: linear-gradient(135deg, #3e4a55, #22282e); }
  .shot--i { grid-column: 3; grid-row: 10 / 13; background: linear-gradient(135deg, #5a4535, #2a221c); }

  .section-label {
    position: absolute; left: 0; top: 318px;
    width: 110px; height: 150px;
    background: var(--label-bg);
    color: var(--white);
    font-weight: 300; font-size: 28px; line-height: 1.05;
    padding: 48px 0 0 10px;
  }
  .story-copy {
    position: absolute; left: 154px; top: 319px;
    width: 400px;
    column-count: 2; column-gap: 12px;
    font-size: 9.4px; line-height: 1.2; color: var(--ink-soft);
  }
  .story-copy h3 { font-size: 9.4px; font-weight: 700; color: var(--ink); }
  .story-copy ul { list-style: none; }
  .story-copy li { padding-left: 8px; text-indent: -8px; }
  .story-copy li::before { content: "- "; }

  /* Event page */
  .page--event { background: #1c1428; }
  .event-photo {
    position: absolute; inset: 0;
    background:
      radial-gradient(ellipse at 40% 90%, rgba(220,60,170,0.55), transparent 55%),
      radial-gradient(ellipse at 55% 30%, rgba(120,90,200,0.6), transparent 60%),
      linear-gradient(180deg, #3b2a6a 0%, #24163f 55%, #2a1230 100%);
  }
  .event-title {
    position: absolute; left: 50px; top: 70px;
    color: var(--white); font-size: 44px; line-height: 1; font-weight: 300;
  }
  .event-title strong { font-weight: 700; display: block; }
  .event-panel {
    position: absolute; left: 338px; top: 92px;
    width: 222px; height: 348px;
    background: var(--panel);
    color: var(--white);
    padding: 24px 20px 0 20px;
    font-size: 9.4px; line-height: 1.2;
  }
  .event-panel h3 { font-size: 9.4px; font-weight: 700; }
  .event-panel p { margin-bottom: 10px; text-align: justify; }
  .event-panel ul { list-style: none; margin-bottom: 10px; }
  .event-panel li { padding-left: 8px; text-indent: -8px; }
  .event-panel li::before { content: "- "; }
</style>
</head>
<body>
  <main class="spread">
    <section class="page page--story">
      <div class="collage">
        <div class="shot shot--a" role="img" aria-label="Interview still: man in a dark suit speaking"></div>
        <div class="shot shot--b" role="img" aria-label="Interview still: woman in front of a city window"></div>
        <div class="shot shot--c" role="img" aria-label="Interview still: woman with glasses"></div>
        <div class="shot shot--d" role="img" aria-label="Interview still: woman in a market"></div>
        <div class="shot shot--e" role="img" aria-label="Interview still: man gesturing in a studio"></div>
        <div class="shot shot--f" role="img" aria-label="Interview still: man in a shop"></div>
        <div class="shot shot--g" role="img" aria-label="Interview still: woman smiling"></div>
        <div class="shot shot--h" role="img" aria-label="Interview still: man in a dark jacket"></div>
        <div class="shot shot--i" role="img" aria-label="Interview still: bearded man in a workshop"></div>
      </div>

      <h2 class="section-label">Your<br>STORY</h2>

      <div class="story-copy">
        <h3>Video Profile</h3>
        <p>The Your STORY video profile is a combination of interviews and overlay footage designed to tell your business' story.</p>
        <p>This style of video content helps your audience better understand:</p>
        <ul>
          <li>what makes you unique</li>
          <li>why they should trust you</li>
          <li>what your product offering is and how it works</li>
          <li>what your process is</li>
        </ul>
        <p>We'll work with you to develop the best approach to deliver this in a sharp &amp; engaging fashion.</p>
        <p>The package includes:</p>
        <ul>
          <li>Filming of interviews + overlay footage at your desired location</li>
          <li>A slick, professionally edited high definition video</li>
          <li>Quick turnaround time and review process</li>
          <li>An opportunity to make any changes before your video is finalised</li>
          <li>Delivery in your choice of formats</li>
        </ul>
        <p>Have additional requirements? No problem. Contact us to discuss a quote.</p>
      </div>
    </section>

    <section class="page page--event">
      <div class="event-photo" role="img" aria-label="Guests dancing at an evening party under purple and pink stage lights"></div>
      <h2 class="event-title">Your<strong>EVENT</strong></h2>
      <div class="event-panel">
        <h3>Event Coverage &amp; Highlights</h3>
        <p>Got a launch, seminar, celebration, party or any other event that you want filmed? We've got you covered.</p>
        <p>The Your EVENT package provides creative event coverage, with the best parts of your event condensed into a slick highlights video that captures the vibe and essence of your event.</p>
        <p style="margin-bottom:0">The package includes:</p>
        <ul>
          <li>Filming of your event exactly as you need</li>
          <li>A slick, professionally edited high definition video, cut to music to suit your event</li>
          <li>An opportunity to review an edit and make changes before your video is finalised</li>
          <li>Delivery in your choice of formats</li>
          <li>Speech &amp; speaker recording also available</li>
        </ul>
        <p>Have additional requirements? No problem. Contact us to discuss a quote.</p>
      </div>
    </section>
  </main>
</body>
</html>
```